Funny (3Romp-alike) Site Design + Code Needed

Hello everybody,

I'm newcomer who want to make a site that could generate income in the future.
I'm interested in funny photo sites like 3romp.
So I need:

- An website that works like 3romp (users post images, comments...)
- The website should have ability to crawl images from 3romp posts then post in my site(every x min/hrs)...
- The web graphic should be design to be clean, fresh, neat as well as there are spots for ads.

In sum, I need an autopilot 3romp-alike site.
I think there are alot of source that looks like 3romp. So the main point here is to design it unique, and make it autopilot.

Any question, please inbox me.
Thanks.

```html
<!DOCTYPE html>
<html lang="en">
<head>
<meta charset="utf-8">
<title>Giggle Nest</title>
<link rel="stylesheet" href="https://fonts.googleapis.com/css2?family=Source+Sans+3:wght@400;600;700&display=swap">
<style>
:root{
  --sky-top:#3aa6ee;
  --sky-bottom:#cfe8fa;
  --page:#f3f4f5;
  --white:#ffffff;
  --orange:#f7890f;
  --orange-dark:#e46f00;
  --blue:#1b8fc9;
  --navy:#1a5379;
  --title-blue:#2183b4;
  --text:#6b6b6b;
  --text-dark:#3c3c3c;
  --footer-top:#3ba3e0;
  --footer-bottom:#1d7fc0;
}
*{box-sizing:border-box;margin:0;padding:0}
html,body{width:1200px;height:2387px;overflow:hidden}
body{position:relative;background:var(--page);font-family:"Source Sans 3",Arial,sans-serif;color:var(--text)}
.abs{position:absolute}
.hero{left:0;top:0;width:1200px;height:640px;background:linear-gradient(180deg,var(--sky-top) 0%,#74c0f3 45%,var(--sky-bottom) 78%,var(--page) 100%)}
.header{left:115px;top:0;width:970px;height:108px;background:var(--white);box-shadow:0 3px 8px rgba(0,0,0,.12)}
.brand-name{left:31px;top:22px;font-size:36px;font-weight:700;color:var(--orange);line-height:1;white-space:nowrap}
.brand-tag{left:91px;top:63px;font-size:16px;color:var(--blue);line-height:1}
.nav{left:390px;top:36px;display:flex;font-size:19px;color:#555;line-height:1}
.nav span{padding:0 22px;border-left:1px solid #bbb}
.nav span:first-child{border-left:none;padding-left:0}
.btn{top:32px;height:30px;border-radius:3px;color:#fff;font-size:13px;font-weight:700;text-align:center;line-height:30px}
.btn-login{left:762px;width:78px;background:var(--orange)}
.btn-upload{left:849px;width:88px;background:var(--blue)}
.hero-title{left:0;top:254px;width:1200px;text-align:center;font-size:37px;font-weight:600;color:var(--navy)}
.hero-sub{left:250px;top:302px;width:700px;text-align:center;font-size:19px;line-height:22px;color:#3e5b70}
.card{background:var(--white);border:1px solid #e6e6e6}
.video-title{font-size:18px;font-weight:600;color:var(--orange);line-height:1}
.small{font-size:12px;line-height:19px;color:var(--text)}
.meta-line{font-size:12px;color:var(--text-dark)}
.photo{border:1px solid #ddd}
.post-title{font-size:24px;font-weight:400;color:var(--title-blue);line-height:1}
.post-meta{font-size:11.5px;color:var(--title-blue);text-transform:uppercase}
.post-text{font-size:12.5px;line-height:21px;color:var(--text)}
.actions{display:flex;align-items:center;font-size:12.5px;color:var(--text-dark);gap:10px}
.share{display:flex;gap:4px}
.share i{display:block;width:22px;height:22px;border-radius:3px}
.divider{border-top:2px dotted #c8c8c8}
.side-head{background:linear-gradient(180deg,var(--orange),var(--orange-dark));color:#fff;font-size:21px;padding:16px 22px;height:53px}
.side-item{display:flex;gap:14px;height:99px}
.side-thumb{width:103px;height:76px;border:3px solid #f0f0f0}
.side-item-title{font-size:14px;color:var(--text-dark)}
.side-item-text{font-size:11.5px;line-height:19px;color:#999}
.ad{overflow:hidden}
.ad-badge{background:var(--blue);color:#fff;font-weight:600}
.page-btn{width:24px;height:24px;border:1px solid #ccc;border-radius:3px;font-size:12px;text-align:center;line-height:22px;color:#555;background:#fafafa}
.page-btn.active{background:var(--orange);border-color:var(--orange);color:#fff}
.page-btn.arrow{color:var(--orange)}
.footer{left:0;top:2271px;width:1200px;height:116px;background:linear-gradient(180deg,var(--footer-top),var(--footer-bottom))}
.footer-links{left:120px;top:30px;font-size:15px;color:#fff}
.footer-links span{padding:0 10px;border-left:1px solid rgba(255,255,255,.7)}
.footer-links span:first-child{padding-left:0;border:none}
.copy{left:120px;top:60px;font-size:12px;color:#e1f1fb}
.social{left:951px;top:34px;display:flex;gap:5px}
.social i{display:block;width:28px;height:28px;border-radius:50%;background:#fff;opacity:.9}
</style>
</head>
<body>

<div class="abs hero"></div>

<header class="abs header">
  <div class="abs brand-name">Giggle Nest</div>
  <div class="abs brand-tag">Salogan goes here</div>
  <nav class="abs nav"><span>HOT</span><span>FRESH</span><span>TREDING</span><span>MORE</span></nav>
  <div class="abs btn btn-login">LOGIN</div>
  <div class="abs btn btn-upload">UPLOAD</div>
</header>

<section class="slider">
  <svg class="abs" style="left:110px;top:275px" width="62" height="62" viewBox="0 0 62 62"><circle cx="31" cy="31" r="27" fill="none" stroke="#fff" stroke-width="4"/><path d="M35 20 L24 31 L35 42" fill="none" stroke="#fff" stroke-width="5"/></svg>
  <div class="abs hero-title">Mauris vel lacus vitae felis vestibulum volutpat</div>
  <div class="abs hero-sub">Etiam est nunc, venenatis in, tristique eu, imperdiet ac, nisl. Cum sociis natoque penatibus et magnis dis parturient montes</div>
  <svg class="abs" style="left:1026px;top:275px" width="62" height="62" viewBox="0 0 62 62"><circle cx="31" cy="31" r="27" fill="none" stroke="#fff" stroke-width="4"/><path d="M27 20 L38 31 L27 42" fill="none" stroke="#fff" stroke-width="5"/></svg>
</section>

<section class="abs card videos" style="left:115px;top:512px;width:660px;height:288px">
  <div class="abs" style="left:17px;top:20px;width:205px">
    <div class="photo" role="img" aria-label="Video still: person in a blue hoodie at a shop counter" style="height:126px;background:linear-gradient(135deg,#7a4a2a,#3d5e9a 60%,#2a2a2a)"></div>
    <div class="video-title" style="margin-top:12px">Duis tincidunt lectus</div>
    <div class="small" style="margin-top:4px">Mauris vel lacus vitae felis vestibulum volutpat. Etiam est nunc, venenatis in, tristique eu, imperdiet ac, nisl.</div>
    <div class="meta-line" style="margin-top:9px">28 Comments &nbsp;|&nbsp; Add a Comment</div>
  </div>
  <div class="abs" style="left:230px;top:20px;width:205px">
    <div class="photo" role="img" aria-label="Video still: street scene with trees and a truck" style="height:126px;background:linear-gradient(135deg,#5d5a3e,#8a8d78 55%,#3d3b30)"></div>
    <div class="video-title" style="margin-top:12px">Duis tincidunt lectus</div>
    <div class="small" style="margin-top:4px">Mauris vel lacus vitae felis vestibulum volutpat. Etiam est nunc, venenatis in, tristique eu, imperdiet ac, nisl.</div>
    <div class="meta-line" style="margin-top:9px">28 Comments &nbsp;|&nbsp; Add a Comment</div>
  </div>
  <div class="abs" style="left:443px;top:20px;width:200px">
    <div class="photo" role="img" aria-label="Video still: night road with lights" style="height:126px;background:linear-gradient(135deg,#1d1f1a,#4a4a35 55%,#15160f)"></div>
    <div class="video-title" style="margin-top:12px">Duis tincidunt lectus</div>
    <div class="small" style="margin-top:4px">Mauris vel lacus vitae felis vestibulum volutpat. Etiam est nunc, venenatis in, tristique eu, imperdiet ac, nisl.</div>
    <div class="meta-line" style="margin-top:9px">28 Comments &nbsp;|&nbsp; Add a Comment</div>
  </div>
  <svg class="abs" style="left:100px;top:64px" width="40" height="40" viewBox="0 0 40 40"><circle cx="20" cy="20" r="18" fill="#222" stroke="#fff" stroke-width="3"/><path d="M16 12 L28 20 L16 28Z" fill="#fff"/></svg>
  <svg class="abs" style="left:313px;top:64px" width="40" height="40" viewBox="0 0 40 40"><circle cx="20" cy="20" r="18" fill="#222" stroke="#fff" stroke-width="3"/><path d="M16 12 L28 20 L16 28Z" fill="#fff"/></svg>
  <svg class="abs" style="left:525px;top:64px" width="40" height="40" viewBox="0 0 40 40"><circle cx="20" cy="20" r="18" fill="#222" stroke="#fff" stroke-width="3"/><path d="M16 12 L28 20 L16 28Z" fill="#fff"/></svg>
</section>

<main class="abs card posts" style="left:115px;top:816px;width:660px;height:1452px">
  <article class="abs" style="left:19px;top:30px;width:625px">
    <h2 class="post-title">Phasellus felis dolor scelerisque a tempus eget</h2>
    <div class="post-meta" style="margin-top:9px">October 30, 2013 | In: Awesome, Funny, Morning Awesomeness</div>
    <div role="img" aria-label="Photo: young German shepherd puppy sitting in a car" style="margin-top:14px;height:236px;background:linear-gradient(120deg,#9a9a96,#5a4a36 45%,#2c2622 70%,#7d7b78)"></div>
    <p class="post-text" style="margin-top:14px">Vivamus porttitor, g, purus nisi eleifend libero, a tempus libero lectus feugiat felis. Morbi diam mauris, viverra in, gravida eu, mattis in, ante. Morbi eget arcu. Morbi porta, libero id ullamcorper nonummy, nibh ligula pulvinar metus, eget consectetuer augue nisi quis lacus. Ut ac mi quis lacus mollis aliquam.</p>
    <div class="actions" style="margin-top:9px">52 Comments <span>|</span> Learn More <span>|</span> Add a Comment
      <span class="share"><i style="background:#3b5998"></i><i style="background:#1da1f2"></i><i style="background:#d34836"></i><i style="background:#cb2027"></i><i style="background:#27a352"></i></span></div>
  </article>
  <div class="abs divider" style="left:25px;top:461px;width:612px"></div>

  <article class="abs" style="left:22px;top:483px;width:625px">
    <h2 class="post-title">Phasellus felis dolor scelerisque a tempus eget</h2>
    <div class="post-meta" style="margin-top:9px">October 30, 2013 | In: Awesome, Funny, Morning Awesomeness</div>
    <div role="img" aria-label="Photo: pigeons perched on a man resting in a beach chair" style="margin-top:14px;height:235px;background:linear-gradient(180deg,#9c9285,#b8a68e 50%,#a48a6e)"></div>
    <p class="post-text" style="margin-top:14px">Vivamus porttitor, g, purus nisi eleifend libero, a tempus libero lectus feugiat felis. Morbi diam mauris, viverra in, gravida eu, mattis in, ante. Morbi eget arcu. Morbi porta, libero id ullamcorper nonummy, nibh ligula pulvinar metus, eget consectetuer augue nisi quis lacus. Ut ac mi quis lacus mollis aliquam.</p>
    <div class="actions" style="margin-top:9px">52 Comments <span>|</span> Learn More <span>|</span> Add a Comment
      <span class="share"><i style="background:#3b5998"></i><i style="background:#1da1f2"></i><i style="background:#d34836"></i><i style="background:#cb2027"></i><i style="background:#27a352"></i></span></div>
  </article>
  <div class="abs divider" style="left:25px;top:917px;width:612px"></div>

  <article class="abs" style="left:19px;top:942px;width:625px">
    <h2 class="post-title">Phasellus felis dolor scelerisque a tempus eget</h2>
    <div class="post-meta" style="margin-top:9px">October 30, 2013 | In: Awesome, Funny, Morning Awesomeness</div>
    <div role="img" aria-label="Photo: sleepy dog cuddling a baby on a sofa" style="margin-top:14px;height:236px;background:linear-gradient(120deg,#6b5548,#c9a06a 40%,#8a7a70 70%,#5e4a44)"></div>
    <p class="post-text" style="margin-top:14px">Vivamus porttitor, g, purus nisi eleifend libero, a tempus libero lectus feugiat felis. Morbi diam mauris, viverra in, gravida eu, mattis in, ante. Morbi eget arcu. Morbi porta, libero id ullamcorper nonummy, nibh ligula pulvinar metus, eget consectetuer augue nisi quis lacus. Ut ac mi quis lacus mollis aliquam.</p>
    <div class="actions" style="margin-top:9px">52 Comments <span>|</span> Learn More <span>|</span> Add a Comment
      <span class="share"><i style="background:#3b5998"></i><i style="background:#1da1f2"></i><i style="background:#d34836"></i><i style="background:#cb2027"></i><i style="background:#27a352"></i></span></div>
  </article>

  <nav class="abs pagination" style="left:230px;top:1394px;display:flex;gap:9px">
    <div class="page-btn arrow">«</div>
    <div class="page-btn active">1</div>
    <div class="page-btn">2</div>
    <div class="page-btn">3</div>
    <div class="page-btn arrow">»</div>
  </nav>
</main>

<aside class="abs card most-viewed" style="left:786px;top:512px;width:299px;height:685px;border-top:none">
  <div class="side-head">MOST VIEWED</div>
  <div class="abs" style="left:26px;top:70px">
    <div class="side-item"><div class="side-thumb" role="img" aria-label="Thumbnail: performer on stage" style="background:linear-gradient(135deg,#2a1a1a,#b04a3a)"></div><div><div class="side-item-title">Mauris vel lacus</div><div class="side-item-text">felis vestibulum volutpat.<br>Etiam est nunc venenatis<br>in tristique eu</div></div></div>
    <div class="side-item"><div class="side-thumb" role="img" aria-label="Thumbnail: dancers in the dark" style="background:linear-gradient(135deg,#0c0c0c,#505050)"></div><div><div class="side-item-title">Mauris vel lacus</div><div class="side-item-text">felis vestibulum volutpat.<br>Etiam est nunc venenatis<br>in tristique eu</div></div></div>
    <div class="side-item"><div class="side-thumb" role="img" aria-label="Thumbnail: group of people posing" style="background:linear-gradient(135deg,#3a2a22,#c49a80)"></div><div><div class="side-item-title">Mauris vel lacus</div><div class="side-item-text">felis vestibulum volutpat.<br>Etiam est nunc venenatis<br>in tristique eu</div></div></div>
    <div class="side-item"><div class="side-thumb" role="img" aria-label="Thumbnail: wide-angle street view" style="background:linear-gradient(135deg,#8aa4c4,#44566e)"></div><div><div class="side-item-title">Mauris vel lacus</div><div class="side-item-text">felis vestibulum volutpat.<br>Etiam est nunc venenatis<br>in tristique eu</div></div></div>
    <div class="side-item"><div class="side-thumb" role="img" aria-label="Thumbnail: portrait of a woman" style="background:linear-gradient(135deg,#3a1f24,#c07a7a)"></div><div><div class="side-item-title">Mauris vel lacus</div><div class="side-item-text">felis vestibulum volutpat.<br>Etiam est nunc venenatis<br>in tristique eu</div></div></div>
    <div class="side-item"><div class="side-thumb" role="img" aria-label="Thumbnail: people relaxing indoors" style="background:linear-gradient(135deg,#4a3a4e,#b08a76)"></div><div><div class="side-item-title">Mauris vel lacus</div><div class="side-item-text">felis vestibulum volutpat.<br>Etiam est nunc venenatis<br>in tristique eu</div></div></div>
  </div>
</aside>

<aside class="abs ad" style="left:787px;top:1210px;width:298px;height:245px;background:linear-gradient(180deg,#b8d0de,#e4eef2)">
  <div class="abs" style="left:20px;top:10px;font-size:14px;color:#333">UP TO</div>
  <div class="abs" style="left:20px;top:22px;font-size:40px;color:#222;line-height:1.1">15% OFF</div>
  <div class="abs" style="left:20px;top:66px;font-size:15px;color:#222">ON SELECT LAPTOPS</div>
  <div class="abs ad-badge" style="left:220px;top:10px;font-size:12px;padding:3px 8px">Shopcart</div>
  <div class="abs" role="img" aria-label="Laptop product photo" style="left:50px;top:100px;width:200px;height:110px;background:linear-gradient(135deg,#1e2a2e,#4b6a6e 60%,#222)"></div>
  <div class="abs" style="left:190px;top:213px;background:#222;color:#fff;font-size:12px;padding:4px 10px">SHOP NOW »</div>
</aside>

<aside class="abs ad" style="left:787px;top:1466px;width:298px;height:250px;background:linear-gradient(180deg,#5a2a5a,#c42a5a)">
  <div class="abs" style="left:28px;top:6px;font-size:39px;color:#fff;font-weight:700">BEST PRICES</div>
  <div class="abs" style="left:30px;top:52px;width:250px;text-align:center;font-size:16px;color:#fff;line-height:17px">ON LAPTOPS WITH THE BEST CONFIGURATIONS</div>
  <div class="abs" role="img" aria-label="Two laptops product photo" style="left:30px;top:100px;width:240px;height:110px;background:linear-gradient(135deg,#2a2a2a,#8a8a8a 55%,#3a3a3a)"></div>
  <div class="abs ad-badge" style="left:10px;top:212px;font-size:14px;padding:5px 10px">Shopcart</div>
  <div class="abs" style="left:190px;top:218px;background:#333;color:#fff;font-size:12px;padding:4px 10px">SHOP NOW »</div>
</aside>

<footer class="abs footer">
  <div class="abs footer-links"><span>Home</span><span>About</span><span>Post</span><span>Support</span><span>Contact Us</span></div>
  <div class="abs copy">© 2013 Company Name. &nbsp;All right reserved. &nbsp;Term of Use</div>
  <div class="abs social"><i></i><i></i><i></i><i></i></div>
</footer>

</body>
</html>
```